Brambleway Farming

We need a logo design for a new company based in Kelowna, BC. We grow market garden vegetables for sale at market and in a CSA program. We try to only use hand tools for all aspects of cultivating, seeding, weeding, harvesting and distributing. For this reason we consider ourselves very low impact on the environment.

We would like blues and green in the design with an earthy, natural feel

Target Market(s)

Environmentally aware, health conscience

Industry/Entity Type

Farming

Requirements
Must have
• Foot prints with section for contact details all on the one side
Should not have
• Dark, black colours or anything that looks unnatural

```html
<!DOCTYPE html>
<html lang="en">
<head>
<meta charset="utf-8">
<title>Brambleway Farming – Business Card</title>
<link href="https://fonts.googleapis.com/css2?family=Open+Sans:wght@400;600;700&display=swap" rel="stylesheet">
<style>
  :root {
    --backdrop: #3c3c3c;
    --card-dark: #050505;
    --leaf: #8cbf00;
    --leaf-soft: #9bca1a;
    --leaf-deep: #7fae00;
    --ink-light: #e8e8e8;
    --white: #ffffff;
  }
  * { margin: 0; padding: 0; box-sizing: border-box; }
  html, body {
    width: 1200px; height: 900px; overflow: hidden;
    background: var(--backdrop);
    font-family: "Open Sans", sans-serif;
  }
  .canvas { position: relative; width: 1200px; height: 900px; }
  .card {
    position: absolute; top: 170px; width: 346px; height: 560px; overflow: hidden;
  }
  .card--contact { left: 259px; background: var(--card-dark); }
  .card--brand { left: 631px; background: var(--leaf); }

  .band { position: absolute; left: 0; width: 346px; }
  .band--top { top: 0; }
  .band--bottom { bottom: 0; }

  .emblem-area {
    position: absolute; left: 92px; top: 95px; width: 162px; height: 180px;
    border-radius: 40px;
    background: radial-gradient(ellipse at center, #6f9a00 0%, #2c3d00 60%, var(--card-dark) 100%);
    opacity: 0.9;
  }

  .contact { position: absolute; left: 0; right: 0; top: 334px; text-align: center; color: var(--ink-light); }
  .contact__name { color: var(--leaf); font-weight: 700; font-size: 21px; letter-spacing: 0.3px; line-height: 28px; }
  .contact__role { font-size: 14.5px; line-height: 20px; }
  .contact__lines { margin-top: 14px; font-size: 14.5px; line-height: 21px; }
  .contact__label { color: var(--leaf); font-weight: 700; margin-right: 4px; }
  .contact__address { margin-top: 12px; font-size: 14.5px; line-height: 17px; }

  .backdrop-decor {
    position: absolute; inset: 0;
    background:
      radial-gradient(ellipse 110px 230px at 80px 330px, var(--leaf-soft) 0%, rgba(155,202,26,0) 100%),
      radial-gradient(ellipse 110px 230px at 270px 330px, var(--leaf-soft) 0%, rgba(155,202,26,0) 100%);
  }
  .brand-name {
    position: absolute; left: 0; right: 0; top: 254px; text-align: center;
    color: var(--white); font-weight: 700; font-size: 30px; line-height: 36px;
  }
  .tagline {
    position: absolute; left: 0; right: 0; top: 450px; text-align: center;
    color: var(--white); font-weight: 700; font-size: 16px; line-height: 29px;
  }
</style>
</head>
<body>
<main class="canvas">
  <section class="card card--contact">
    <svg class="band band--top" width="346" height="50" viewBox="0 0 346 50">
      <path d="M103 0 H245 V48 Q174 30 103 48 Z" fill="var(--leaf)"/>
    </svg>
    <div class="emblem-area" role="img" aria-label="Brand emblem area"></div>
    <div class="contact">
      <p class="contact__name">ALDER FINCH</p>
      <p class="contact__role">Managing Director</p>
      <div class="contact__lines">
        <p><span class="contact__label">P:</span>250-555-0148</p>
        <p><span class="contact__label">E:</span>hello@bramblewayfarm.ca</p>
        <p><span class="contact__label">W:</span>www.bramblewayfarm.ca</p>
      </div>
      <p class="contact__address">4820 Orchard Lane Kelowna<br>BC, V1W 2K7</p>
    </div>
    <svg class="band band--bottom" width="346" height="30" viewBox="0 0 346 30">
      <path d="M103 30 H245 V4 Q174 -6 103 4 Z" fill="var(--leaf)"/>
    </svg>
  </section>

  <section class="card card--brand">
    <div class="backdrop-decor" role="img" aria-label="Soft background decoration"></div>
    <h1 class="brand-name">Brambleway<br>Farming</h1>
    <p class="tagline">CULTIVATING, SEEDING, WEEDING,<br>HARVESTING AND DISTRIBUTING</p>
  </section>
</main>
</body>
</html>
```